Design 2015 Winter themed holiday card

We need a holiday card for our company.

The attached brief provides all the information for the design. We provided two images for the cover or if you have something better.

CARD DESIGN 4" x 6" Vertical Folded Card
Bleed: The extra .0625" on each side of your artwork that bleeds off the edge of the piece and ensures your piece will not end up with white borders.
Trim: The final size the printed piece will be.
Safe: The .0625" area from the final trim size. Do not place text or important imagery beyond the safe line to avoid it getting cut off when the finished piece is trimmed to final size.
Corner Rounding, where available, can be 1/8" or 5/16". Examples are provided in the image below.
1/8" is a "tighter" or "smaller" corner radius.
5/16" is a "wider" or "larger" corner radius.

Target Market(s)

Government agencies, businesses and nonprofits

Industry/Entity Type

It Company

Font styles to use
Serif
Sans Serif

Requirements
Must have
• Please follow the design brief: KQRB-Strategy-Brief-Holiday-Card-11042015.pdf
• It includes the fonts, colors, design parameters - please review it before designing. I've included two previous holiday cards for your review.
• Please add "Seasons Greetings" on the cover.

```html
<!DOCTYPE html>
<html lang="en">
<head>
<meta charset="utf-8">
<title>KQRB Holiday Card</title>
<link rel="stylesheet" href="https://fonts.googleapis.com/css2?family=Dancing+Script:wght@700&family=EB+Garamond:wght@400&family=Josefin+Sans:wght@300&family=Mrs+Saint+Delafield&family=Nothing+You+Could+Do&family=Kaushan+Script&family=Caveat:wght@400&family=Parisienne&display=swap">
<style>
  :root {
    --page-bg: #d4d6d9;
    --paper: #ffffff;
    --sky-top: #2459cc;
    --sky-mid: #4a80dc;
    --sky-low: #8fb2ea;
    --hills: #3e6fcf;
    --hills-dark: #2f5cb8;
    --snow-field: #b9d0f3;
    --lake: #7ea3e4;
    --lake-light: #cfe0f8;
    --ink-blue: #3a5aa6;
    --holiday-blue: #3a8ad0;
    --message-grey: #8b9096;
    --fold-line: #d9dce0;
    --signature-ink: #2a2a2a;
    --signature-faint: #6b6b6b;
  }
  * { box-sizing: border-box; margin: 0; padding: 0; }
  html, body { width: 908px; height: 1200px; overflow: hidden; }
  body { background: var(--page-bg); position: relative; }

  .spread {
    position: absolute;
    left: 94px;
    width: 720px;
    height: 540px;
    background: var(--paper);
    border-radius: 14px;
    overflow: hidden;
    display: flex;
  }
  .spread--outside { top: 40px; }
  .spread--inside { top: 620px; }

  .panel { position: relative; width: 360px; height: 100%; }

  /* Outside: back panel */
  .back-panel { display: flex; flex-direction: column; align-items: center; justify-content: flex-end; padding-bottom: 46px; }
  .brand { display: flex; align-items: center; gap: 8px; margin-bottom: 8px; }
  .brand__dot { width: 14px; height: 14px; border-radius: 50%; background: var(--ink-blue); }
  .brand__name { font-family: "EB Garamond", serif; font-size: 30px; color: var(--ink-blue); letter-spacing: 2px; }
  .contact { font-family: "EB Garamond", serif; font-size: 13.5px; line-height: 1.45; color: var(--ink-blue); text-align: center; }

  /* Outside: cover panel */
  .cover-panel {
    background: linear-gradient(180deg,
      var(--sky-top) 0%,
      var(--sky-mid) 42%,
      var(--sky-low) 60%,
      var(--hills) 64%,
      var(--hills-dark) 72%,
      var(--snow-field) 76%,
      var(--lake) 84%,
      var(--lake-light) 92%,
      var(--snow-field) 100%);
  }
  .cover-art { position: absolute; inset: 0; }
  .cover-title { position: absolute; top: 54px; left: 0; right: 0; text-align: center; color: #fff; }
  .cover-title__main { font-family: "Dancing Script", cursive; font-size: 32px; line-height: 1; }
  .cover-title__sub { font-family: "EB Garamond", serif; font-size: 17px; margin-top: 4px; }

  /* Inside: signatures */
  .sign-panel { border-right: 1px solid var(--fold-line); }
  .signature { position: absolute; white-space: nowrap; color: var(--signature-ink); line-height: 1; }
  .signature--owen { left: 56px; top: 150px; font-family: "Mrs Saint Delafield", cursive; font-size: 40px; transform: rotate(-22deg); }
  .signature--adrian { left: 185px; top: 118px; font-family: "Mrs Saint Delafield", cursive; font-size: 36px; transform: rotate(7deg); }
  .signature--mira { left: 120px; top: 200px; font-family: "Mrs Saint Delafield", cursive; font-size: 40px; transform: rotate(-4deg); }
  .signature--daniel { left: 50px; top: 315px; font-family: "Kaushan Script", cursive; font-size: 18px; transform: rotate(-12deg); }
  .signature--nora { left: 208px; top: 278px; font-family: "Parisienne", cursive; font-size: 32px; transform: rotate(-14deg); }
  .signature--priya { left: 118px; top: 375px; font-family: "Caveat", cursive; font-size: 26px; transform: rotate(4deg); }
  .signature--tessa { left: 222px; top: 418px; font-family: "Kaushan Script", cursive; font-size: 24px; transform: rotate(3deg); }
  .signature--helena { left: 115px; top: 478px; font-family: "Nothing You Could Do", cursive; font-size: 16px; color: var(--signature-faint); transform: rotate(-6deg); }

  /* Inside: message */
  .message-panel { display: flex; flex-direction: column; align-items: center; padding-top: 200px; }
  .message { font-family: "Josefin Sans", sans-serif; font-weight: 300; font-variant: small-caps; font-size: 15px; line-height: 1.45; color: var(--message-grey); text-align: center; letter-spacing: 0.5px; }
  .message + .message { margin-top: 22px; }
  .message__holiday { display: block; font-family: "Dancing Script", cursive; font-variant: normal; font-size: 22px; line-height: 1.05; color: var(--holiday-blue); }
</style>
</head>
<body>
  <section class="spread spread--outside">
    <div class="panel back-panel">
      <div class="brand">
        <span class="brand__dot"></span>
        <span class="brand__name">KQRB</span>
      </div>
      <p class="contact">
        KQRB Communications, LLC<br>
        418 Linden Avenue, Suite 300<br>
        Harlow, MD 21090<br>
        800-555-0142<br>
        kqrbcomms.com
      </p>
    </div>
    <div class="panel cover-panel">
      <div class="cover-art" role="img" aria-label="Winter illustration: falling snow over blue hills, a snow-covered cabin with a lit window and a frozen lake"></div>
      <div class="cover-title">
        <p class="cover-title__main">Seasons Greetings</p>
        <p class="cover-title__sub">from Our New Perch</p>
      </div>
    </div>
  </section>

  <section class="spread spread--inside">
    <div class="panel sign-panel">
      <span class="signature signature--owen">Owen Pratt</span>
      <span class="signature signature--adrian">Adrian Solano</span>
      <span class="signature signature--mira">Mira Jonkers</span>
      <span class="signature signature--daniel">Daniel Forster</span>
      <span class="signature signature--nora">Nora Bales</span>
      <span class="signature signature--priya">Priya Holden</span>
      <span class="signature signature--tessa">Tessa Marlow</span>
      <span class="signature signature--helena">Helena Vosburg</span>
    </div>
    <div class="panel message-panel">
      <p class="message">As this year draws to a close,<br>we are grateful for the opportunities<br>we have had to work together.</p>
      <p class="message">We wish you all the best for the year to come.<br><span class="message__holiday">Happy Holidays</span>from the KQRB team</p>
    </div>
  </section>
</body>
</html>
```